Packaging & Label Design for CDB Products

We are a European CBD company specialising in athletic recovery, sleep improvement and wellness.

We would like the packaging to incorporate our logo and name (and font 'Codec') 'Meridell CBD'. The design must be transferable to all of our products. CBD Oils, Balms, Lip Balm and Vape E-Liquid.

We would like it to be simple but eye-catching and modern. We don't want bright colours. Preferred pallet of muted greys, blacks, white and pastel colours. Geometric concepts, possibly using different colours for each item of the range, we are open to new and fresh ideas (we are seeking you for your experience) and when we find the right design we would likely throw more work in your direction..

Our product range is not complete so the designer must be flexible with some changes and provide files where format can be easily edited by packaging manufacturer. We are also waiting for dimensions for the labels and boxes for several products and will supply the designer with full dimensions of all products once selected.

Oil Box: 2.6 x 9.0 x 2.6 cm (open format 16.7 x 11.6cm)
Labels: 7.8 x 3.3 cm (Front and Back)

Our expected product range will be:
CBD Oil 1000mg
CBD Oil 3000mg
CBD Balm 100mg
CBD Balm 300mg
E-Liquid 500mg
Lip Balm 50mg

We look forward to seeing your ideas.

Best Regards
Meridell CBD

```html
<!DOCTYPE html>
<html lang="en">
<head>
<meta charset="utf-8">
<title>Meridell CBD – Full Spectrum CBD Oil Packaging</title>
<link rel="stylesheet" href="https://fonts.googleapis.com/css2?family=Montserrat:wght@400;500;600;700&display=swap">
<style>
  :root {
    --canvas-bg: #f4f4f4;
    --pack-black: #151515;
    --accent-green: #3f9e6c;
    --text-light: #dcdcdc;
    --shadow: rgba(0, 0, 0, 0.12);
  }
  * { box-sizing: border-box; margin: 0; padding: 0; }
  html, body {
    width: 1200px;
    height: 1200px;
    overflow: hidden;
    background: var(--canvas-bg);
    font-family: "Montserrat", sans-serif;
  }
  .canvas {
    position: relative;
    width: 1200px;
    height: 1200px;
  }

  /* Shared brand lockup */
  .brand {
    display: flex;
    align-items: center;
    justify-content: center;
    gap: 12px;
    color: var(--accent-green);
    font-weight: 600;
    letter-spacing: 0.08em;
    text-transform: uppercase;
  }
  .brand-dot {
    width: 12px;
    height: 12px;
    border-radius: 50%;
    background: var(--accent-green);
  }

  .product-type {
    color: var(--text-light);
    font-weight: 500;
  }
  .product-name {
    color: var(--accent-green);
    font-weight: 700;
    line-height: 1;
  }
  .product-strength,
  .product-spec {
    color: var(--text-light);
    font-weight: 500;
  }

  /* Box front panel */
  .box-front {
    position: absolute;
    left: 640px;
    top: 90px;
    width: 340px;
    height: 1020px;
    background: var(--pack-black);
    box-shadow: 0 20px 40px var(--shadow);
    text-align: center;
  }
  .box-band {
    position: absolute;
    left: 0;
    width: 100%;
    height: 6px;
    background: var(--accent-green);
  }
  .box-band--top { top: 28px; }
  .box-band--bottom { bottom: 64px; }
  .box-front .brand {
    position: absolute;
    top: 200px;
    width: 100%;
    font-size: 28px;
  }
  .box-front .product-info {
    position: absolute;
    top: 390px;
    width: 100%;
  }
  .box-front .product-type { font-size: 24px; }
  .box-front .product-name { font-size: 52px; margin: 10px 0 8px; }
  .box-front .product-strength { font-size: 23px; }
  .box-front .product-specs {
    position: absolute;
    bottom: 150px;
    width: 100%;
  }
  .box-front .product-spec { font-size: 22px; line-height: 1.6; }

  /* Bottle label front */
  .bottle-label {
    position: absolute;
    left: 200px;
    top: 500px;
    width: 380px;
    height: 520px;
    background: var(--pack-black);
    box-shadow: 0 20px 40px var(--shadow);
    text-align: center;
  }
  .bottle-label .brand {
    position: absolute;
    top: 80px;
    width: 100%;
    font-size: 24px;
  }
  .bottle-label .product-info {
    position: absolute;
    top: 190px;
    width: 100%;
  }
  .bottle-label .product-type { font-size: 22px; }
  .bottle-label .product-name { font-size: 46px; margin: 8px 0 6px; }
  .bottle-label .product-strength { font-size: 20px; }
  .bottle-label .product-specs {
    position: absolute;
    bottom: 80px;
    width: 100%;
  }
  .bottle-label .product-spec { font-size: 19px; line-height: 1.6; }
</style>
</head>
<body>
<main class="canvas">

  <section class="bottle-label" aria-label="Bottle label, front">
    <div class="brand"><span class="brand-dot"></span>Meridell CBD</div>
    <div class="product-info">
      <p class="product-type">Full Spectrum</p>
      <h2 class="product-name">CBD OIL</h2>
      <p class="product-strength">1000mg CBD</p>
    </div>
    <div class="product-specs">
      <p class="product-spec">10% Hemp Extract</p>
      <p class="product-spec">0.5 fl.oz | 10ml</p>
    </div>
  </section>

  <section class="box-front" aria-label="Oil box, front panel">
    <div class="box-band box-band--top"></div>
    <div class="brand"><span class="brand-dot"></span>Meridell CBD</div>
    <div class="product-info">
      <p class="product-type">Full Spectrum</p>
      <h1 class="product-name">CBD OIL</h1>
      <p class="product-strength">1000mg CBD</p>
    </div>
    <div class="product-specs">
      <p class="product-spec">10% Hemp Extract</p>
      <p class="product-spec">0.5 fl.oz | 10ml</p>
    </div>
    <div class="box-band box-band--bottom"></div>
  </section>

</main>
</body>
</html>
```